Kettle Ledger Business Card design

We need a stand out business card design for Accounting practice based in Australia specialising in pubs, clubs and hotels. We help venues maximise margins, create time and manage cashflow. One club we have been working with for the last 6 months has increased revenue by 3% and margin by 5% in this time frame. We have a back office outsourced system that costs less than having a full time employee and also allows the venues the added benefit of:<br/>-using the office space to become a revenue generating opportunity. <br/>-a complete system to enhance governance, accountability and efficiency within their operation<br/>-52 weeks cover so no hassle to cover annual/sick .. leave<br/><br/>We would like to see designs that use the colours of our logo (green & blue).
Target Market(s)
Australian Pubs, Clubs & Hotels abookkeeping, accounting and tax services
Industry/Entity Type
Accountant
Contact Information for Business Card
Miriam Oakley CPA
Principal
Accountant Tax Agent
Miriam@KettleLedger-example.com.au
0418693142
www.kettleledger-example.com.au
Accounting / Payroll / Tax / SMSF / Technology
Colors
Designer to choose colors to be used in the design.
Look and feel
Each slider illustrates characteristics of the customer's brand and the style your logo design should communicate.

```html
<!DOCTYPE html>
<html lang="en">
<head>
<meta charset="utf-8">
<title>Kettle Ledger Business Card</title>
<link rel="stylesheet" href="https://fonts.googleapis.com/css2?family=Roboto:wght@400;700&display=swap">
<style>
  :root {
    --backdrop: #ececec;
    --card-white: #ffffff;
    --brand-blue: #22408b;
    --brand-green: #0f6b35;
    --text-grey: #7a7a7a;
    --rule-grey: #c9c9c9;
    --on-blue: #ffffff;
  }
  * { box-sizing: border-box; margin: 0; padding: 0; }
  html, body {
    width: 1200px; height: 960px; overflow: hidden;
    background: var(--backdrop);
    font-family: "Roboto", Arial, sans-serif;
  }
  .canvas {
    position: relative; width: 1200px; height: 960px;
  }
  .card {
    position: absolute; left: 250px; width: 700px; height: 400px;
    border-radius: 24px; overflow: hidden;
  }
  .card--front { top: 60px; background: var(--card-white); box-shadow: 0 2px 6px rgba(0,0,0,.08); }
  .card--back { top: 500px; background: var(--brand-blue); }

  /* front */
  .brand {
    position: absolute; left: 58px; top: 142px;
    display: flex; align-items: center; gap: 16px;
  }
  .brand__dot {
    width: 54px; height: 54px; border-radius: 50%;
    background: var(--brand-green);
  }
  .brand__name {
    font-weight: 700; font-size: 42px; line-height: 1;
    color: var(--brand-blue); letter-spacing: -0.5px;
  }
  .divider {
    position: absolute; left: 355px; top: 138px;
    width: 1px; height: 128px; background: var(--rule-grey);
  }
  .contact {
    position: absolute; left: 382px; top: 132px;
  }
  .contact__name {
    font-weight: 700; font-size: 24px; color: var(--brand-blue); line-height: 1.2;
  }
  .contact__role {
    font-size: 17px; color: var(--text-grey); margin-top: 3px; margin-bottom: 12px;
  }
  .contact__line {
    display: flex; align-items: center; gap: 8px;
    font-size: 15.5px; color: var(--text-grey); line-height: 24px;
  }
  .contact__line svg { width: 14px; height: 14px; flex: none; }

  /* back */
  .brand--back {
    position: absolute; left: 0; right: 0; top: 120px;
    display: flex; align-items: center; justify-content: center; gap: 22px;
  }
  .brand--back .brand__dot { width: 80px; height: 80px; }
  .brand--back .brand__name { font-size: 64px; color: var(--on-blue); }
  .services {
    position: absolute; left: 0; right: 0; top: 330px;
    text-align: center; font-size: 18px; color: var(--on-blue);
  }
</style>
</head>
<body>
<main class="canvas">
  <section class="card card--front" aria-label="Card front">
    <div class="brand">
      <span class="brand__dot"></span>
      <span class="brand__name">Kettle<br>Ledger</span>
    </div>
    <div class="divider"></div>
    <div class="contact">
      <p class="contact__name">Miriam Oakley CPA</p>
      <p class="contact__role">Principal, Accountant Tax Agent</p>
      <p class="contact__line">
        <svg viewBox="0 0 16 16" aria-hidden="true"><path d="M4 2 L7 5 L5.5 7 Q7 10 9 10.5 L11 9 L14 12 L12 14 Q4 13 2 4 Z" fill="var(--brand-blue)"/></svg>
        0418693142
      </p>
      <p class="contact__line">
        <svg viewBox="0 0 16 16" aria-hidden="true"><rect x="1.5" y="3.5" width="13" height="9" fill="var(--brand-blue)"/><path d="M1.5 3.5 L8 9 L14.5 3.5" fill="none" stroke="#fff" stroke-width="1.3"/></svg>
        Miriam@KettleLedger-example.com.au
      </p>
      <p class="contact__line">
        <svg viewBox="0 0 16 16" aria-hidden="true"><g fill="none" stroke="var(--brand-blue)" stroke-width="1.3"><circle cx="8" cy="8" r="6.3"/><ellipse cx="8" cy="8" rx="2.8" ry="6.3"/><path d="M1.7 8 H14.3 M3 4.8 H13 M3 11.2 H13"/></g></svg>
        www.kettleledger-example.com.au
      </p>
    </div>
  </section>

  <section class="card card--back" aria-label="Card back">
    <div class="brand brand--back">
      <span class="brand__dot"></span>
      <span class="brand__name">Kettle Ledger</span>
    </div>
    <p class="services">Accounting - Payroll - Tax - SMSF - Technology</p>
  </section>
</main>
</body>
</html>
```